Flyer-Design für Leben am See
Zielgruppe
Der Betrieb vermietet Wohnungen in einer Appartementanlage und Stellplätze für Wohnwägen (in Zukunft Wohncubes) auf einem Campingplatz, wobei die Mieter langfristig bleiben (ab 1 Jahr und länger). Touristen, die kurz- bis mittelfristig einen Wohnwagen/-cube (1 bis 4 Wochen) mieten, sind die Ausnahme. Singles, Paare oder Familien sind die Zielgruppen. Da der Betrieb direkt am See liegt, besteht für Kunden die Möglichkeit, Badekabinen und private Badeplätze anzumieten. Mehr Information unter www.birkenmoos.at
Aufgabenstellung
Das Ziel ist natürlich, die Objekte so attraktiv wie möglich zu präsentieren, und bei den Betrachtern ein positives Gefühl hervorzurufen. Neben den Koordinaten des Betriebes (Lage, Tel, email, etc) soll die Einmaligkeit des Lebens am See in der Anlage dargestellt werden. Es sollen starke Emotionen wie Wärme, Heim, Garten, See, Angekommen sein, ankern und privat zur Ruhe gekommen sein, provoziert werden.

```html
<!DOCTYPE html>
<html lang="de">
<head>
<meta charset="utf-8">
<title>Flyer – Leben am See</title>
<link rel="stylesheet" href="https://fonts.googleapis.com/css2?family=Kalam:wght@400;700&family=EB+Garamond:wght@400;700&display=swap">
<style>
  :root{
    --green:#1f5a3c;
    --green-dark:#1a4f34;
    --brown:#5a3a12;
    --peach:#f9dcc4;
    --sage:#d6dbd4;
    --paper:#ffffff;
    --ink:#2a2a2a;
    --bg:#ece9e4;
  }
  *{box-sizing:border-box;margin:0;padding:0}
  html,body{width:1200px;height:800px;overflow:hidden;background:var(--bg)}
  body{position:relative;font-family:"EB Garamond",serif;color:var(--ink)}
  .spread{position:absolute;top:120px;width:560px;height:560px;background:var(--paper);box-shadow:0 4px 14px rgba(0,0,0,.18);overflow:hidden}
  .spread--outer{left:30px}
  .spread--inner{left:610px}
  .spread::after{content:"";position:absolute;left:279px;top:0;width:2px;height:100%;background:linear-gradient(90deg,rgba(0,0,0,.06),rgba(0,0,0,0))}
  .abs{position:absolute}
  .script{font-family:"Kalam",cursive;color:var(--green);line-height:1.15}
  .body-text{font-size:9.2px;line-height:1.45;text-align:justify;hyphens:auto}
  .body-text p+p{margin-top:5px}
  .photo{position:absolute}

  /* outer spread */
  .cover-photo{left:0;top:0;width:560px;height:330px;background:linear-gradient(180deg,#d5dbe8 0%,#e7e2e4 40%,#e9c7bc 52%,#6b7a86 60%,#3f4f58 75%,#3a3f2f 100%)}
  .cover-title{left:300px;top:40px;font-size:25px;font-weight:700}
  .cover-title span{display:block}
  .cover-title span+span{padding-left:26px}
  .rule{left:0;top:336px;width:560px;height:2px;background:var(--green)}
  .info{left:22px;top:350px;width:240px}
  .info h2{font-family:"Kalam",cursive;color:var(--green);font-size:15px;font-weight:700;margin-bottom:6px}
  .offer{left:290px;top:346px;width:120px;height:110px;background:var(--peach);padding:10px 8px;font-size:13px}
  .offer li{list-style:none;line-height:1.1;margin-bottom:5px}
  .offer li::before{content:"· "}
  .brand{left:420px;top:346px;width:140px;height:110px;display:flex;flex-direction:column;align-items:center;justify-content:center;gap:8px}
  .brand-mark{width:40px;height:40px;background:var(--green)}
  .brand-name{font-family:"EB Garamond",serif;font-weight:700;font-size:15px;letter-spacing:.5px;color:var(--green)}
  .promo{left:285px;top:466px;width:125px;height:94px;background:var(--brown);color:#fff;font-family:"Kalam",cursive;font-size:14px;line-height:1.15;padding:14px 10px;text-align:center}
  .contact{left:420px;top:466px;width:140px;height:94px;background:var(--green);color:#fff;font-size:8.6px;line-height:1.35;padding:8px 10px}

  /* inner spread */
  .welcome{left:0;top:0;width:280px;height:172px;background:linear-gradient(180deg,#eef0f4,#f6f3f2);padding:26px 20px}
  .welcome h1{font-family:"Kalam",cursive;font-weight:700;color:var(--green);font-size:19px;line-height:1.2}
  .welcome h1+h1{margin-top:10px}
  .apartment{left:0;top:172px;width:280px;height:120px;background:var(--peach);padding:12px 20px}
  .apartment h2,.camping h2{font-family:"Kalam",cursive;color:var(--green);font-size:14px;font-weight:700;margin-bottom:5px}
  .strip{left:0;top:292px;width:280px;height:8px;background:#d9d6d0}
  .cabin-band{left:0;top:300px;width:280px;height:46px;background:var(--brown);color:#fff;font-family:"Kalam",cursive;font-size:13.5px;line-height:1.15;padding:6px 18px}
  .cabin{left:10px;top:352px;width:262px}
  .cabin-photo{float:left;width:92px;height:160px;margin:0 10px 4px 0;background:linear-gradient(180deg,#6b5f52,#a89a86 60%,#7a7264)}
  .ph-family{left:284px;top:4px;width:136px;height:190px;background:linear-gradient(160deg,#e8c9b0,#d9a88e 55%,#b9c4cc)}
  .ph-lake{left:424px;top:4px;width:132px;height:190px;background:linear-gradient(180deg,#9aa862 0%,#5d6f74 35%,#2e3a44 100%)}
  .ph-pier{left:284px;top:198px;width:276px;height:214px;background:linear-gradient(180deg,#8fb6dc 0%,#c9dbe9 25%,#6f9a5a 38%,#6fa1aa 50%,#9fc2bd 75%,#b2b58e 100%)}
  .frame{left:280px;top:0;width:280px;height:412px;background:var(--peach)}
  .camping{left:280px;top:412px;width:280px;height:148px;background:var(--sage);padding:18px 20px}
</style>
</head>
<body>

<section class="spread spread--outer">
  <div class="photo cover-photo" role="img" aria-label="Seeufer bei Abenddämmerung mit kahlem Baum, Schilf und Bergen"></div>
  <h1 class="abs script cover-title"><span>Erleben Sie traumhaftes</span><span>Wohnen direkt am Irrsee</span></h1>
  <div class="abs rule"></div>

  <div class="abs info">
    <h2>Allgemeine Informationen</h2>
    <div class="body-text">
      <p>Fischer oder Bootsbesitzer können sich einen eigenen Platz am See mieten.<br>Zwei großzügige und gepflegte Badeplätze stehen den Familien zur Verfügung. Abhängig von der Kombination unseres Angebotes und Ihren Wünschen machen wir ein Anbot auf Anfrage.</p>
      <p>Der Betrieb liegt verkehrstechnisch optimal zwischen der Westbahn (5 Min.) und der Westautobahn (10 Min.) Für Information über die verschiedenen Pakete besuchen Sie bitte unsere Website www.birkenmoos.at oder rufen Sie uns an!</p>
    </div>
  </div>

  <ul class="abs script offer">
    <li>Appartements</li>
    <li>Camping/ Wohncubes</li>
    <li>private Kabinen &amp; Badeplätze</li>
  </ul>

  <div class="abs brand">
    <div class="brand-mark"></div>
    <div class="brand-name">BIRKENMOOS</div>
  </div>

  <div class="abs promo">Urlaub oder langfristige Miete möglich!</div>

  <address class="abs contact" style="font-style:normal">
    Birkenmoos Betriebs GmbH<br>Birkenmoos 30<br>4893 Seewinkel<br>Tel: + 43 6200 4417<br>info@birkenmoos.at<br>www.birkenmoos.at
  </address>
</section>

<section class="spread spread--inner">
  <div class="abs welcome">
    <h1>Ankommen. Runterkommen. Durchatmen!</h1>
    <h1>Genießen Sie alle Vorzüge dieser wunderbaren Lage.</h1>
  </div>

  <div class="abs apartment">
    <h2>Mieten Sie ein Appartement!</h2>
    <div class="body-text">
      <p>Wenn Sie eine gemütliche Atmosphäre mit Blick auf den Irrsee oder Dachstein suchen, dann finden Sie bei uns die richtige Wohnung.<br>Die Appartements haben 2 Zimmer samt Nebenräume und sind mit Küche, Bad und Kabel TV ausgestattet.<br>Jede Wohnung verfügt über einen Parkplatz.</p>
    </div>
  </div>

  <div class="abs strip"></div>
  <h2 class="abs cabin-band">Ihre private Kabine und ein eigener Badeplatz in erster Reihe – perfekt!</h2>

  <div class="abs cabin body-text">
    <div class="cabin-photo" role="img" aria-label="Holzwand einer Badekabine"></div>
    <p>Die sommerlichen Badefreuden ergänzt eine private Kabine, wo alle Badesachen verstaut werden können. Unsere neuen Kabinen sind mit Strom, Licht und - falls gewünscht - mit Wasser ausgestattet.</p>
    <p>Die Kabinen können in Kombination mit einem privaten Badeplatz mit eigenen Einstieg in den See kombiniert werden. In dieser gepflegten Privatatmosphäre lässt sich die Sommerfrische angenehm in Ruhe genießen.</p>
  </div>

  <div class="abs frame"></div>
  <div class="photo ph-family" role="img" aria-label="Familie mit Kindern am See"></div>
  <div class="photo ph-lake" role="img" aria-label="Kind blickt über Schilf auf den See"></div>
  <div class="photo ph-pier" role="img" aria-label="Holzsteg im klaren Seewasser vor grünen Hügeln"></div>

  <div class="abs camping">
    <h2>Oder doch lieber Camping?</h2>
    <div class="body-text">
      <p>Die großzügigen Plätze für Wohnwägen und Zelte liegen direkt am See. Für Familien und Fischer der ideale Platz, wo man entspannen und leben kann.<br>Wasser, Abwasser, Strom und TV sind bei jedem einzelnen Platz installiert.</p>
    </div>
  </div>
</section>

</body>
</html>
```